Fun relaxed Travel Photography Business Card*

Require a fun, funky and quirky but rememberable business card for a travel photographer

Industry/Entity Type

Photographer

Contact Information for Business Card

Front Card

(my name) Tavo M.

Travel Photographer ( small under travel photographer) “self-proclaimed”

(website logo) wanderingtavo.example

(Instagram logo) @wandering_with_tavo

(Instagram logo) @wandering_with_tavo_2.0 (backup for when Instagram puts Tavo on timeout for bad behaviour)

Tel: N/A (removing the potential awkwardness of me not replying)

Email: (see above)

Back Card

Offending people since 1986

(Bottom right corner) “p.s. travelling made me fatTER”

Font styles to use
Serif

Colors

Designer to choose colors to be used in the design.

Requirements
Must have
• a camera
• a similar cartoon version of me as the "logo" see attached files, try to make as similar as possible

```html
<!DOCTYPE html>
<html lang="en">
<head>
<meta charset="utf-8">
<title>Tavo M. – Travel Photographer Business Card</title>
<link rel="stylesheet" href="https://fonts.googleapis.com/css2?family=Prata&family=Prompt:wght@600&display=swap">
<style>
  :root {
    --card-blue: #3a51a2;
    --sun-yellow: #e5b72a;
    --ring-gold: #bb9c4c;
    --shadow-grey: #c8c8c8;
    --page-white: #ffffff;
    --serif: "Prata", Georgia, serif;
    --sans: "Prompt", Arial, sans-serif;
  }
  * { margin: 0; padding: 0; box-sizing: border-box; }
  html, body {
    width: 1200px; height: 1200px; overflow: hidden;
    background: var(--page-white);
  }
  .canvas { position: relative; width: 1200px; height: 1200px; }

  .card {
    position: absolute; top: 282px;
    width: 362px; height: 634px;
    background: var(--card-blue);
    box-shadow: 7px 8px 0 var(--shadow-grey);
    overflow: hidden;
    color: var(--sun-yellow);
  }
  .card--front { left: 199px; }
  .card--back { left: 638px; }

  /* Front */
  .accent-dot {
    position: absolute; left: 25px; top: 25px;
    width: 18px; height: 18px; border-radius: 50%;
    background: var(--sun-yellow);
  }
  .name {
    position: absolute; left: 24px; top: 50px;
    font-family: var(--serif); font-size: 23px; line-height: 1; font-weight: 400;
  }
  .rule {
    position: absolute; height: 2.5px; background: var(--sun-yellow);
  }
  .card--front .rule { left: 26px; top: 85px; width: 313px; }
  .title {
    position: absolute; left: 25px; top: 97px;
    font-family: var(--serif); font-size: 14.5px; line-height: 1;
  }
  .title-note {
    position: absolute; left: 23px; top: 118px;
    font-family: var(--serif); font-size: 10.5px; line-height: 1;
  }
  .portrait-badge {
    position: absolute; left: 29px; top: 164px;
    width: 304px; height: 304px;
  }
  .contact-list { list-style: none; }
  .contact {
    position: absolute; left: 26px;
    display: flex; align-items: center; gap: 16px;
    font-family: var(--serif); font-size: 14px; line-height: 1;
  }
  .contact--web { top: 500px; }
  .contact--social-main { top: 540px; }
  .contact--social-backup { top: 581px; }
  .contact-mark {
    width: 34px; height: 34px; border-radius: 50%;
    background: var(--sun-yellow); flex: none;
    display: flex; align-items: center; justify-content: center;
  }

  /* Back */
  .corner-portrait {
    position: absolute; left: 225px; top: -10px;
    width: 150px; height: 175px;
    border-radius: 50% 0 50% 50%;
    background: radial-gradient(circle at 60% 40%, rgba(229,183,42,0.55), rgba(229,183,42,0.15) 70%, rgba(229,183,42,0) 100%);
  }
  .tagline {
    position: absolute; left: 0; right: 0; top: 294px;
    text-align: center;
    font-family: var(--serif); font-size: 18.5px; line-height: 1;
  }
  .card--back .rule { left: 26px; top: 333px; width: 309px; }
  .postscript {
    position: absolute; right: 27px; top: 596px;
    font-family: var(--sans); font-weight: 600; font-size: 10.5px; line-height: 1;
  }
</style>
</head>
<body>
<main class="canvas">

  <section class="card card--front" aria-label="Business card front">
    <span class="accent-dot"></span>
    <h1 class="name">Tavo M.</h1>
    <span class="rule"></span>
    <p class="title">Travel Photographer</p>
    <p class="title-note">[ Self - Proclaimed ]</p>

    <svg class="portrait-badge" viewBox="0 0 304 304">
      <circle cx="152" cy="152" r="152" fill="var(--ring-gold)"/>
      <circle cx="152" cy="152" r="133" fill="var(--sun-yellow)"/>
      <circle cx="152" cy="152" r="117" fill="var(--sun-yellow)" stroke="var(--card-blue)" stroke-width="2.5"
              role="img" aria-label="Cartoon portrait of Tavo with round glasses and a jacket"/>
    </svg>

    <ul class="contact-list">
      <li class="contact contact--web">
        <span class="contact-mark">
          <svg width="22" height="22" viewBox="0 0 22 22" fill="none" stroke="var(--card-blue)" stroke-width="1.6" aria-hidden="true">
            <circle cx="11" cy="11" r="9.5"/>
            <ellipse cx="11" cy="11" rx="4" ry="9.5"/>
            <line x1="1.5" y1="11" x2="20.5" y2="11"/>
            <line x1="3" y1="6.5" x2="19" y2="6.5"/>
            <line x1="3" y1="15.5" x2="19" y2="15.5"/>
          </svg>
        </span>
        wanderingtavo.example
      </li>
      <li class="contact contact--social-main">
        <span class="contact-mark"></span>
        @wandering_with_tavo
      </li>
      <li class="contact contact--social-backup">
        <span class="contact-mark"></span>
        @wandering_with_tavo_2.0
      </li>
    </ul>
  </section>

  <section class="card card--back" aria-label="Business card back">
    <div class="corner-portrait" role="img" aria-label="Cartoon head of Tavo peeking in from the corner, wearing round glasses"></div>
    <p class="tagline">Offending People Since 1986</p>
    <span class="rule"></span>
    <p class="postscript">P. S. Travelling Made Me FatTER</p>
  </section>

</main>
</body>
</html>
```